Business Card design for shipping company 'FERNHOLT INTERNATIONAL LTD'

Classic / traditional business card in black Garamond / Times New Roman or similar text for a shipping / marine transport company, containing the following information:

QUOTE

FERNHOLT INTERNATIONAL LTD

MARTIN QUESTEDGE FICS

T: +44 7902 615370
E: cargo@fernholt-example.com

UNQUOTE

Target Market(s)

Marine / Shipping industry

Contact Information for Business Card

FERNHOLT INTERNATIONAL LTD MARTIN QUESTEDGE FICS T: +44 7902 615370 E: cargo@fernholt-example.com

Font styles to use
Serif

Colors

Designer to choose colors to be used in the design.

Requirements
Must have
• Garamond / Times New Roman or similar text in black colour

```html
<!DOCTYPE html>
<html lang="en">
<head>
<meta charset="utf-8">
<title>Fernholt International Ltd – Business Card</title>
<link rel="stylesheet" href="https://fonts.googleapis.com/css2?family=Tinos:wght@400;700&family=Barlow:wght@400&display=swap">
<style>
  :root {
    --page-bg: #ffffff;
    --ink: #000000;
    --caption: #7a7a7a;
    --front-light: #ffffff;
    --front-tint: #dff0fa;
    --front-edge: #b9d3e0;
    --back-deep: #1e51a3;
    --back-mid: #3f86cc;
    --back-glow: #7fcff2;
    --back-ink: #ffffff;
  }
  html, body {
    margin: 0;
    padding: 0;
    width: 1200px;
    height: 1000px;
    overflow: hidden;
    background: var(--page-bg);
  }
  .sheet {
    position: relative;
    width: 1200px;
    height: 1000px;
  }
  .card {
    position: absolute;
    left: 281px;
    width: 638px;
    height: 364px;
    box-sizing: border-box;
    font-family: "Tinos", "Times New Roman", serif;
  }
  .card--front {
    top: 89px;
    border: 1px solid var(--front-edge);
    background: radial-gradient(ellipse 70% 80% at 45% 40%, var(--front-light) 0%, var(--front-light) 25%, var(--front-tint) 100%);
  }
  .card--back {
    top: 548px;
    background: radial-gradient(ellipse 42% 60% at 50% 40%, var(--back-glow) 0%, var(--back-mid) 50%, var(--back-deep) 100%);
  }
  .company {
    position: absolute;
    margin: 0;
    font-weight: 700;
    line-height: 1;
    white-space: nowrap;
  }
  .company__main { display: block; }
  .company__sub { display: block; }
  .card--front .company {
    left: 49px;
    top: 150px;
    color: var(--ink);
  }
  .card--front .company__main { font-size: 37px; letter-spacing: 0.3px; }
  .card--front .company__sub { font-size: 23px; margin-top: 3px; letter-spacing: 0.2px; }
  .card--back .company {
    left: 0;
    right: 0;
    top: 212px;
    text-align: center;
    color: var(--back-ink);
  }
  .card--back .company__main { font-size: 46px; letter-spacing: 0.4px; }
  .card--back .company__sub { font-size: 30px; margin-top: 4px; letter-spacing: 0.3px; }
  .contact {
    position: absolute;
    left: 327px;
    top: 240px;
    color: var(--ink);
  }
  .contact__name {
    margin: 0 0 20px;
    font-size: 21px;
    font-weight: 700;
    letter-spacing: 0.3px;
  }
  .contact__line {
    margin: 0;
    font-size: 19px;
    line-height: 24px;
  }
  .caption {
    position: absolute;
    left: 0;
    width: 1200px;
    text-align: center;
    font-family: "Barlow", "Helvetica Neue", sans-serif;
    font-size: 16px;
    color: var(--caption);
    margin: 0;
  }
  .caption--front { top: 482px; }
  .caption--back { top: 941px; }
</style>
</head>
<body>
<main class="sheet">
  <section class="card card--front" aria-label="Business card front">
    <h1 class="company">
      <span class="company__main">FERNHOLT</span>
      <span class="company__sub">INTERNATIONAL LTD</span>
    </h1>
    <div class="contact">
      <p class="contact__name">MARTIN QUESTEDGE FICS</p>
      <p class="contact__line">T: +44 7902 615370</p>
      <p class="contact__line">E: cargo@fernholt-example.com</p>
    </div>
  </section>
  <p class="caption caption--front">Front Side</p>

  <section class="card card--back" aria-label="Business card back">
    <h2 class="company">
      <span class="company__main">FERNHOLT</span>
      <span class="company__sub">INTERNATIONAL LTD</span>
    </h2>
  </section>
  <p class="caption caption--back">Back Side</p>
</main>
</body>
</html>
```